LM Hair and Beauty flyer

Hello I have hairdressing salon called LM Hair and Beauty.I need flyer with double side pls.On front side I need this picture to be there and under the pisture our full address,tel number and email address( 48 Penwick rd E7 3QD 02084417396 media@lmhairandbeauty.co.uk). And under that shoud be written:Special offers
with 3 different discount squares at the bottom of the flyer.First visite 20% off,Second 15% off, thrd 10% off.At he other side of flyer should be following info:Ladies cut & blowdry with 3 different levels of stylist £45-£65,Gents cut £15-£36,Highlights from £45-£120,Express Blowdry £22-£35,Keratin tretmant £150,Manicure from £14,Pedicure from £25,Shellac from £28

Industry/Entity Type

Salon

```html
<!DOCTYPE html>
<html lang="en">
<head>
<meta charset="utf-8">
<title>LM Hair and Beauty – Flyer</title>
<link href="https://fonts.googleapis.com/css2?family=Jost:wght@400;500;600&family=Arimo:wght@400&display=swap" rel="stylesheet">
<style>
  :root {
    --page-bg: #e4e2de;
    --photo-dark: #3e2c26;
    --photo-mid: #8a7264;
    --photo-light: #d9cfc4;
    --top-veil: rgba(110, 104, 100, 0.55);
    --band-dark: #8c7a50;
    --band-light: #d6c69b;
    --ink: #0d0b0a;
    --paper: #ffffff;
    --footer: #050505;
    --divider: #8a8a8a;
    --icon: #c9c3b8;
  }
  * { margin: 0; padding: 0; box-sizing: border-box; }
  html, body { width: 900px; height: 1200px; overflow: hidden; background: var(--page-bg); }
  .canvas { position: relative; width: 900px; height: 1200px; }

  .flyer {
    position: absolute; left: 30px; top: 20px;
    width: 840px; height: 1160px; overflow: hidden;
    background: var(--band-dark);
    font-family: "Jost", sans-serif;
  }

  .team-photo {
    position: absolute; left: 0; top: 0; width: 840px; height: 714px;
    background:
      radial-gradient(ellipse at 50% 55%, var(--photo-mid) 0%, rgba(138,114,100,0) 60%),
      linear-gradient(180deg, var(--photo-light) 0%, #b7a597 45%, var(--photo-dark) 100%);
  }
  .top-veil {
    position: absolute; left: 0; top: 0; width: 840px; height: 65px;
    background: var(--top-veil);
  }

  .offer-band {
    position: absolute; left: 0; top: 714px; width: 840px; height: 361px;
    background: linear-gradient(160deg, var(--band-dark) 0%, #b2a074 55%, var(--band-light) 100%);
  }

  .offer-tag { position: absolute; top: 689px; width: 209px; height: 318px; }
  .offer-tag svg { position: absolute; inset: 0; }
  .offer-tag--first  { left: 42px; }
  .offer-tag--second { left: 320px; }
  .offer-tag--third  { left: 602px; }
  .offer-tag__text {
    position: absolute; left: 0; top: 44px; width: 209px;
    text-align: center; line-height: 1;
  }
  .offer-tag__title { display: block; color: var(--paper); font-size: 56px; font-weight: 400; letter-spacing: -1px; }
  .offer-tag__sub   { display: block; color: var(--paper); font-size: 52px; font-weight: 400; margin-top: 8px; }
  .offer-tag__value { display: block; color: var(--ink); font-size: 74px; font-weight: 600; margin-top: 10px; letter-spacing: -1px; }

  .contact-bar {
    position: absolute; left: 0; top: 1075px; width: 840px; height: 85px;
    background: var(--footer);
    font-family: "Arimo", sans-serif; font-size: 15px; color: var(--paper);
  }
  .contact-item { position: absolute; top: 0; height: 85px; display: flex; align-items: center; gap: 10px; white-space: nowrap; }
  .contact-item svg { width: 18px; height: 18px; fill: var(--icon); }
  .contact-item--address { left: 192px; }
  .contact-item--phone   { left: 418px; }
  .contact-item--email   { left: 572px; }
  .contact-divider { position: absolute; top: 12px; width: 1px; height: 60px; background: var(--divider); }
  .contact-divider--one { left: 398px; }
  .contact-divider--two { left: 552px; }

  .brand-block {
    position: absolute; left: 0; top: 1047px; width: 177px; height: 113px;
    background: var(--footer);
    display: flex; align-items: center; justify-content: center;
    color: var(--paper); font-family: "Jost", sans-serif; font-weight: 400; text-align: center;
  }
  .brand-block__name { font-size: 19px; line-height: 1.25; }
</style>
</head>
<body>
<div class="canvas">
  <section class="flyer">
    <div class="team-photo" role="img" aria-label="Sepia group photo of the salon team posing inside the salon"></div>
    <div class="top-veil"></div>

    <div class="offer-band"></div>

    <svg width="0" height="0" style="position:absolute" aria-hidden="true">
      <defs>
        <linearGradient id="leather" x1="0" y1="0" x2="0" y2="1">
          <stop offset="0" stop-color="#b98766"/><stop offset="1" stop-color="#8e5f43"/>
        </linearGradient>
      </defs>
    </svg>

    <div class="offer-tag offer-tag--first">
      <svg viewBox="0 0 209 318" aria-hidden="true">
        <polygon points="8,0 201,0 209,22 0,22" fill="#6d4530"/>
        <polygon points="0,22 209,22 209,270 104.5,318 0,270" fill="url(#leather)"/>
        <polygon points="7,30 202,30 202,265 104.5,310 7,265" fill="none" stroke="#f3e4d2" stroke-width="1.5" stroke-dasharray="4 3"/>
      </svg>
      <div class="offer-tag__text">
        <span class="offer-tag__title">First</span>
        <span class="offer-tag__sub">visite</span>
        <span class="offer-tag__value">20%</span>
      </div>
    </div>

    <div class="offer-tag offer-tag--second">
      <svg viewBox="0 0 209 318" aria-hidden="true">
        <polygon points="8,0 201,0 209,22 0,22" fill="#6d4530"/>
        <polygon points="0,22 209,22 209,270 104.5,318 0,270" fill="url(#leather)"/>
        <polygon points="7,30 202,30 202,265 104.5,310 7,265" fill="none" stroke="#f3e4d2" stroke-width="1.5" stroke-dasharray="4 3"/>
      </svg>
      <div class="offer-tag__text">
        <span class="offer-tag__title">Second</span>
        <span class="offer-tag__sub">visite</span>
        <span class="offer-tag__value">15%</span>
      </div>
    </div>

    <div class="offer-tag offer-tag--third">
      <svg viewBox="0 0 209 318" aria-hidden="true">
        <polygon points="8,0 201,0 209,22 0,22" fill="#6d4530"/>
        <polygon points="0,22 209,22 209,270 104.5,318 0,270" fill="url(#leather)"/>
        <polygon points="7,30 202,30 202,265 104.5,310 7,265" fill="none" stroke="#f3e4d2" stroke-width="1.5" stroke-dasharray="4 3"/>
      </svg>
      <div class="offer-tag__text">
        <span class="offer-tag__title">Third</span>
        <span class="offer-tag__sub">visite</span>
        <span class="offer-tag__value">10%</span>
      </div>
    </div>

    <footer class="contact-bar">
      <div class="contact-item contact-item--address">
        <svg viewBox="0 0 20 20" aria-hidden="true"><path d="M10 2 L1 10 H4 V18 H8.5 V13 H11.5 V18 H16 V10 H19 Z"/></svg>
        <span>48 Penwick rd E7 3QD</span>
      </div>
      <span class="contact-divider contact-divider--one"></span>
      <div class="contact-item contact-item--phone">
        <svg viewBox="0 0 20 20" aria-hidden="true"><path d="M5 2 L8 6 L6.5 8 C7.5 10.5 9.5 12.5 12 13.5 L14 12 L18 15 L16 18 C9 18 2 11 2 4 Z"/></svg>
        <span>02084417396</span>
      </div>
      <span class="contact-divider contact-divider--two"></span>
      <div class="contact-item contact-item--email">
        <svg viewBox="0 0 20 20" aria-hidden="true"><path d="M2 5 H18 V15 H2 Z M3 6 L10 11 L17 6" stroke="#050505" stroke-width="1"/></svg>
        <span>media@lmhairandbeauty.co.uk</span>
      </div>
    </footer>

    <div class="brand-block">
      <span class="brand-block__name">LM Hair<br>and Beauty</span>
    </div>
  </section>
</div>
</body>
</html>
```